Bright Lantern Studios Business Card Design

Doug Farley

Managing Partner

Doug@BrightLanternStudios.com

BrightLanternStudios.com

502-417-2356

Industry/Entity Type

Photographer

Contact Information for Business Card

Doug Farley

Managing Partner

Doug@BrightLanternStudios.com

BrightLanternStudios.com

502-417-2356

Requirements
Must have
• Must show that I am a pavlo trusted photographer

```html
<!DOCTYPE html>
<html lang="en">
<head>
<meta charset="utf-8">
<title>Bright Lantern Studios – Business Card</title>
<link rel="stylesheet" href="https://fonts.googleapis.com/css2?family=Jost:wght@500&family=Open+Sans:wght@400;600&display=swap">
<style>
  :root {
    --backdrop: #7a7a7a;
    --card-dark: #000000;
    --card-light: #ffffff;
    --ink-light: #ffffff;
    --ink-dark: #111111;
    --rule: #8a8a8a;
    --badge-fill: #3a3a3a;
  }
  * { margin: 0; padding: 0; box-sizing: border-box; }
  html, body { width: 1200px; height: 900px; overflow: hidden; }
  body { background: var(--backdrop); position: relative; font-family: "Open Sans", Arial, sans-serif; }

  .card {
    position: absolute; top: 307px; width: 438px; height: 270px;
    border-radius: 11px; overflow: hidden;
    box-shadow: 2px 3px 4px rgba(0,0,0,0.45);
  }
  .card--front { left: 150px; background: var(--card-dark); color: var(--ink-light); }
  .card--back { left: 609px; background: var(--card-light); color: var(--ink-dark); }

  .front-brand-dot {
    position: absolute; left: 35px; top: 113px; width: 46px; height: 46px;
    border-radius: 50%; border: 4px solid var(--ink-light);
  }
  .front-brand-name {
    position: absolute; left: 102px; top: 135px;
    transform: translate(-50%, -50%) rotate(-90deg);
    white-space: nowrap;
    font-family: "Jost", Arial, sans-serif; font-weight: 500;
    font-size: 13.5px; letter-spacing: 0.6px; text-transform: uppercase;
  }
  .front-divider {
    position: absolute; left: 142px; top: 76px; width: 1px; height: 124px;
    background: var(--rule);
  }
  .person { position: absolute; left: 157px; top: 84px; }
  .person__name { font-weight: 600; font-size: 17px; line-height: 20px; text-transform: uppercase; }
  .person__role { font-size: 13px; line-height: 18px; }

  .contacts { position: absolute; left: 158px; top: 138px; list-style: none; }
  .contacts__item {
    display: flex; align-items: center; gap: 6px;
    font-size: 13px; line-height: 18.5px; height: 18.5px;
  }
  .contacts__icon { width: 13px; height: 13px; flex: none; }

  .trust-badge {
    position: absolute; left: 360px; top: 222px; width: 66px; height: 24px;
    border-radius: 3px; background: var(--badge-fill);
  }

  .back-brand-dot {
    position: absolute; left: 183px; top: 77px; width: 72px; height: 72px;
    border-radius: 50%; border: 7px solid var(--ink-dark);
  }
  .back-brand-name {
    position: absolute; left: 0; right: 0; top: 168px; text-align: center;
    font-family: "Jost", Arial, sans-serif; font-weight: 500;
    font-size: 22px; letter-spacing: 0.8px; text-transform: uppercase;
  }
</style>
</head>
<body>

  <section class="card card--front">
    <div class="front-brand-dot"></div>
    <div class="front-brand-name">Bright Lantern Studios</div>
    <div class="front-divider"></div>

    <div class="person">
      <p class="person__name">Doug Farley</p>
      <p class="person__role">Managing Partner</p>
    </div>

    <ul class="contacts">
      <li class="contacts__item">
        <svg class="contacts__icon" viewBox="0 0 13 13" aria-hidden="true">
          <rect width="13" height="13" rx="2.5" fill="#fff"/>
          <rect x="4" y="2.2" width="5" height="8.6" rx="1" fill="none" stroke="#000" stroke-width="1.2"/>
          <circle cx="6.5" cy="9" r="0.6" fill="#000"/>
        </svg>
        <span>502-417-2356</span>
      </li>
      <li class="contacts__item">
        <svg class="contacts__icon" viewBox="0 0 13 13" aria-hidden="true">
          <rect width="13" height="13" rx="2.5" fill="#fff"/>
          <rect x="2.3" y="3.5" width="8.4" height="6" fill="none" stroke="#000" stroke-width="1.1"/>
          <path d="M2.5 3.8 L6.5 7 L10.5 3.8" fill="none" stroke="#000" stroke-width="1.1"/>
        </svg>
        <span>Doug@BrightLanternStudios.com</span>
      </li>
      <li class="contacts__item">
        <svg class="contacts__icon" viewBox="0 0 13 13" aria-hidden="true">
          <rect width="13" height="13" rx="2.5" fill="#fff"/>
          <circle cx="6.5" cy="6.5" r="3.8" fill="none" stroke="#000" stroke-width="1.1"/>
          <ellipse cx="6.5" cy="6.5" rx="1.6" ry="3.8" fill="none" stroke="#000" stroke-width="0.9"/>
          <line x1="2.7" y1="6.5" x2="10.3" y2="6.5" stroke="#000" stroke-width="0.9"/>
        </svg>
        <span>www.BrightLanternStudios.com</span>
      </li>
    </ul>

    <div class="trust-badge" role="img" aria-label="Pavlo trusted photographer badge"></div>
  </section>

  <section class="card card--back">
    <div class="back-brand-dot"></div>
    <p class="back-brand-name">Bright Lantern Studios</p>
  </section>

</body>
</html>
```